Webdesign für ambulanter Pflegedienst
Zielgruppe
Es ist ein ambulanter Pflegedienst, der sich im Raum Dessau-Roßlau um die Versorgung sowie Betreuung von Menschen kümmert. Kontaktdaten: ambulanter Pflegedienst Hand Sorge; Inhaberin: Sabine Lohmar; Birkenweg 14, 06871 Dessau-Roßlau Telefon: 034907/519364
IK-Nummer: 47 283 6194
e-mail: sl-hand-sorge@postfeld.de
Aufgabenstellung
Die Farben sollen in Anlehnung an das Logo sein, dass mit übersandt wird.

```html
<!DOCTYPE html>
<html lang="de">
<head>
<meta charset="utf-8">
<title>Sofortige Hilfen – Hand Sorge</title>
<link href="https://fonts.googleapis.com/css2?family=Raleway:wght@400;500;600;700&family=Handlee&display=swap" rel="stylesheet">
<style>
  :root {
    --teal: #46aaa8;
    --teal-soft: #b2dbd8;
    --green: #7cb342;
    --ink: #5e5e5e;
    --ink-dark: #555;
    --sky: #dcedf7;
    --white: #ffffff;
    --line: #e4e4e4;
  }
  * { margin: 0; padding: 0; box-sizing: border-box; }
  html, body { width: 733px; height: 1200px; overflow: hidden; background: var(--white); }
  body { position: relative; font-family: "Raleway", sans-serif; color: var(--ink); }
  .abs { position: absolute; }
  .script { font-family: "Handlee", cursive; }

  .site-header { left: 0; top: 0; width: 733px; height: 30px; background: var(--white); }
  .brand { left: 162px; top: 5px; display: flex; align-items: center; gap: 3px; font-size: 5.5px; font-weight: 600; color: var(--ink); }
  .brand-dot { width: 9px; height: 9px; border-radius: 50%; background: var(--teal); }
  .main-nav { left: 256px; top: 10px; display: flex; gap: 0; font-size: 8px; }
  .main-nav span { position: absolute; white-space: nowrap; }
  .main-nav .active { color: var(--green); font-weight: 600; }

  .tagline-band { left: 0; top: 30px; width: 733px; height: 16px; background: var(--sky); text-align: center; font-size: 6.5px; line-height: 16px; }
  .tagline-band b { color: var(--teal); font-weight: 500; }

  .hero { left: 0; top: 46px; width: 733px; height: 111px; background: linear-gradient(90deg, #acd9d6 0%, #d8ebe5 40%, #f2f1ec 55%, #f2f1ec 56%); }
  .hero-photo { left: 409px; top: 46px; width: 324px; height: 111px; background: linear-gradient(90deg, rgba(242,241,236,0) 0%, #c9b9a6 25%, #6b4a34 45%, #d9d5cf 60%, #7a5a44 80%, #3e2c22 100%); }
  .hero-kicker { left: 161px; top: 79px; font-size: 10px; }
  .hero-title { left: 161px; top: 94px; font-size: 19.5px; font-weight: 700; color: var(--ink-dark); }
  .hero-badge { left: 436px; top: 99px; width: 88px; height: 88px; border-radius: 50%; background: var(--white); box-shadow: 0 2px 5px rgba(0,0,0,.12); display: flex; align-items: center; justify-content: center; }

  .service-card { background: var(--white); border: 1px solid var(--line); border-radius: 4px; box-shadow: 0 1px 4px rgba(0,0,0,.08); overflow: hidden; }
  .card-photo { position: absolute; top: 0; bottom: 0; }
  .card-body { position: absolute; }
  .card-title { font-size: 18px; font-weight: 600; color: var(--teal); white-space: nowrap; }
  .card-rule { width: 61px; height: 1.5px; background: var(--green); margin: 8px 0 12px 1px; }
  .card-text { font-size: 7.45px; line-height: 9.55px; }
  .card-text p + p { margin-top: 9.55px; }

  .cta-kicker { left: 0; width: 733px; top: 890px; text-align: center; font-size: 10px; }
  .cta-title { left: 0; width: 733px; top: 905px; text-align: center; font-size: 17px; font-weight: 700; color: var(--ink-dark); }
  .cta-button { left: 312px; top: 945px; width: 109px; height: 28px; border-radius: 14px; background: var(--teal); color: var(--white); font-size: 7px; font-weight: 700; text-align: center; line-height: 28px; box-shadow: 0 1px 3px rgba(0,0,0,.15); }

  .site-footer { left: 0; top: 1028px; width: 733px; height: 144px; background: linear-gradient(90deg, #acd9d6 0%, #d8ebe5 35%, #eef0ea 55%); }
  .footer-photo { left: 430px; top: 1028px; width: 303px; height: 144px; background: linear-gradient(90deg, rgba(238,240,234,0) 0%, #d8c3ad 30%, #b58f6f 55%, #4f6a8a 80%, #6a7f97 100%); }
  .footer-kicker { left: 160px; top: 1044px; font-size: 12px; }
  .footer-address { left: 160px; top: 1069px; font-size: 7.6px; line-height: 11.5px; }
  .footer-address .gap { height: 6px; }
  .footer-brand { left: 316px; top: 1078px; width: 100px; text-align: center; }
  .footer-brand .brand-dot { width: 30px; height: 30px; margin: 0 auto 7px; }
  .footer-brand span { font-size: 10.5px; font-weight: 600; color: var(--ink); }
  .to-top { left: 508px; top: 992px; width: 64px; height: 64px; border-radius: 50%; background: var(--sky); text-align: center; font-size: 7.5px; padding-top: 12px; }

  .legal-bar { left: 0; top: 1172px; width: 733px; height: 28px; background: var(--sky); font-size: 6px; font-weight: 700; color: var(--ink-dark); }
  .legal-bar span { position: absolute; top: 10px; white-space: nowrap; }
  .legal-bar .copy { font-weight: 400; font-size: 5.2px; top: 11px; }
</style>
</head>
<body>

<header class="site-header abs">
  <div class="brand abs"><span class="brand-dot"></span>HAND SORGE</div>
  <nav class="main-nav abs">
    <span style="left:0">Startseite</span>
    <span class="active" style="left:52px">Sofortige Hilfen</span>
    <span style="left:125px">Unsere Leistungen</span>
    <span style="left:208px">Karriere</span>
    <span style="left:253px">Pflegekurse</span>
  </nav>
</header>

<div class="tagline-band abs"><b>Hand Sorge</b> - <span class="script">Pflege von Mensch zu Mensch</span></div>

<section class="hero abs"></section>
<div class="hero-photo abs" role="img" aria-label="Foto: Pflegerin begleitet einen älteren Herrn beim Gehen"></div>
<div class="hero-kicker abs script">Wie können wir Ihnen helfen?</div>
<h1 class="hero-title abs">Sofortige Hilfen</h1>
<div class="hero-badge abs">
  <svg width="44" height="44" viewBox="0 0 44 44" fill="none" stroke="#666" stroke-width="2.4">
    <circle cx="22" cy="22" r="20"/>
    <circle cx="22" cy="22" r="9"/>
    <path d="M8 8 L15.6 15.6 M36 8 L28.4 15.6 M8 36 L15.6 28.4 M36 36 L28.4 28.4"/>
  </svg>
</div>

<article class="service-card abs" style="left:161px;top:217px;width:411px;height:281px;">
  <div class="card-photo" style="left:0;width:161px;background:linear-gradient(160deg,#7a6a55 0%,#c89a6a 35%,#8fa9a6 70%,#3c3a36 100%);" role="img" aria-label="Foto: Pflegerin kümmert sich lächelnd um eine Seniorin"></div>
  <div class="card-body" style="left:181px;top:28px;width:212px;">
    <h2 class="card-title">Überleitungspflege</h2>
    <div class="card-rule"></div>
    <div class="card-text">
      <p>Ist ihr Angehöriger gerade im Krankenhaus oder in einer Rehaklinik? Soll dieser demnächst entlassen werden? Es sind jedoch noch so viele Fragen offen, die noch geklärt werden müssen? Fühlen sie sich unsicher, bei dem was auf sie zukommen wird? Dann rufen Sie uns an! Wir helfen Ihnen im Rahmen der Überleitungspflege, dass die Verlegung aus dem Krankenhaus, Pflegeheim oder der Rehaklinik für alle Beteiligten so angenehm wie möglich gestaltet wird. Die Überleitungspflege wurde von den Pflegekassen zur Verfügung gestellt, damit nach der Entlassung aus dem Krankenhaus eine erneute Aufnahme wegen unzureichender pflegerischer und medizinischer Versorgung vermieden werden kann (Drehtür-Effekt). Die Kosten werden komplett von der Pflegekasse getragen. Dieses Angebot gilt für jeden Angehörigen, der aus dem Krankenhaus entlassen wird. Ein Pflegegrad ist nicht notwendig. Daher rufen Sie uns einfach an und wir helfen Ihnen den Übergang in die neue häusliche Situation so angenehm wie möglich zu gestalten.</p>
    </div>
  </div>
</article>

<article class="service-card abs" style="left:161px;top:514px;width:411px;height:330px;">
  <div class="card-body" style="left:21px;top:26px;width:214px;">
    <h2 class="card-title">Individuelle Schulungen</h2>
    <div class="card-rule"></div>
    <div class="card-text">
      <p>Sie sind wichtig! Die Herausforderungen unserer Gesellschaft ist es sich mit der wachsenden Anzahl an pflegebedürftigen Menschen auseinanderzusetzen. Die Verantwortung wird zu einem Großteil auf pflegende Angehörige und Ehrenamtliche übertragen. Zu den pflegenden Angehörigen gehören Personen aus dem Familien-, Freundes- oder Bekanntenkreis eines pflegebedürftigen Menschen, die diesen im häuslichen Bereich ganz oder teilweise im Sinne der Laienpflege versorgen und betreuen. Durch die Übernahme der Pflege stoßen diese Menschen häufig an körperliche und psychische Grenzen. Wir können Ihnen helfen! Im Rahmen von individuellen Schulungen informieren wir Sie gern über Unterstützungsangebote. In diesen Schulungen können wir Ihnen wissen vermitteln, das Ihnen hilft die Pflegetätigkeit in der häuslichen Umgebung des Pflegebedürftigen angenehmer zu gestalten. Die Pflegekasse übernimmt die Kosten komplett.</p>
      <p>Das Thema dieser individuellen Schulung bestimmen ganz sie. Das bedeutet, wenn sie eine Unterweisung im Gebrauch von Hilfsmitteln oder für bestimmte Pflegetätigkeiten benötigen, dann sprechen Sie uns an. Wir richten uns ganz nach ihnen! Unser Ziel ist es sie als pflegenden Angehörigen zu unterstützen!</p>
    </div>
  </div>
  <div class="card-photo" style="left:256px;right:0;background:linear-gradient(170deg,#e9e9e7 0%,#d9dcdc 40%,#b9bcbc 70%,#4a4240 100%);" role="img" aria-label="Foto: Ärztin leitet eine Schulung vor Teilnehmenden"></div>
</article>

<div class="cta-kicker abs script">Wir sind für Sie da</div>
<h2 class="cta-title abs">Sie benötigen Sofortige Hilfen?</h2>
<div class="cta-button abs">Kontakt aufnehmen</div>

<footer class="site-footer abs"></footer>
<div class="footer-photo abs" role="img" aria-label="Foto: Hände, die einander halten"></div>
<div class="footer-kicker abs script">Wir sind für Sie da!</div>
<address class="footer-address abs" style="font-style:normal">
  ambulanter Pflegedienst Hand Sorge<br>
  Inhaberin: Sabine Lohmar<br>
  Birkenweg 14<br>
  06871 Dessau-Roßlau
  <div class="gap"></div>
  034907/519364<br>
  sl-hand-sorge@postfeld.de
</address>
<div class="footer-brand abs"><div class="brand-dot"></div><span>HAND SORGE</span></div>
<div class="to-top abs script">
  <svg width="12" height="20" viewBox="0 0 12 20"><path d="M6 0 L12 10 H7.5 V19 H4.5 V10 H0 Z" fill="#46aaa8"/></svg><br>
  Nach oben
</div>

<div class="legal-bar abs">
  <span style="left:168px">KARRIERE</span>
  <span style="left:226px">KONTAKT</span>
  <span style="left:287px">DATENSCHUTZ</span>
  <span style="left:364px">IMPRESSUM</span>
  <span class="copy" style="left:432px">Copyright 2023 © ambulanter Pflegedienst Hand Sorge</span>
</div>

</body>
</html>
```